CRPG is needing business cards, and stationary created.

Pixel Forge created a logo for our business, and now we are wanting business cards, and stationary. I have included two designs of the same logo. Please feel free to use them as you want. The name of the company is Cedar Ridge Property Group LLC, the address is 812 NE Tamber Ln., Suite 9, the city & state is Bend, Oregon, zip code is 97815, Telephone number is 541-237-4190, Fax number is 541-237-8856, the name on the business card is Travis Lundqor CMCA

Industry/Entity Type

Property Management

Contact Information for Business Card

The card needs to look professional. Upscale.

Requirements
Must have
• The colors we are using are on the logo that has been uploaded.

```html
<!DOCTYPE html>
<html lang="en">
<head>
<meta charset="utf-8">
<title>Cedar Ridge Property Group – Business Card</title>
<link rel="stylesheet" href="https://fonts.googleapis.com/css2?family=Exo+2:wght@600;700&family=Saira+Semi+Condensed:wght@500&family=Roboto:wght@400&display=swap">
<style>
  :root {
    --backdrop: #2b2b2b;
    --paper: #ffffff;
    --slate: #3d4a5a;
    --teal: #1a8c79;
    --ink-light: #ffffff;
  }
  * { margin: 0; padding: 0; box-sizing: border-box; }
  html, body {
    width: 1125px;
    height: 1200px;
    overflow: hidden;
    background: var(--backdrop);
  }
  .canvas {
    position: relative;
    width: 1125px;
    height: 1200px;
  }
  .card {
    position: absolute;
    left: 150px;
    width: 825px;
    box-shadow: 0 6px 18px rgba(0,0,0,0.45);
  }
  .card-front {
    top: 98px;
    height: 472px;
    background: var(--paper);
  }
  .brand {
    position: absolute;
    top: 0;
    left: 0;
    right: 0;
    height: 302px;
    display: flex;
    align-items: center;
    justify-content: center;
    gap: 16px;
  }
  .brand-square {
    width: 26px;
    height: 26px;
    background: var(--teal);
  }
  .brand-name {
    font-family: "Exo 2", sans-serif;
    font-weight: 700;
    font-size: 40px;
    color: var(--teal);
    letter-spacing: 0.5px;
  }
  .name-band {
    position: absolute;
    top: 302px;
    left: 0;
    right: 0;
    height: 59px;
    background: var(--slate);
    display: flex;
    align-items: center;
    justify-content: center;
  }
  .holder-name {
    font-family: "Exo 2", sans-serif;
    font-weight: 700;
    font-size: 29px;
    color: var(--ink-light);
    letter-spacing: 0.5px;
  }
  .contact-band {
    position: absolute;
    top: 365px;
    left: 0;
    right: 0;
    bottom: 0;
    background: var(--teal);
    display: flex;
    flex-direction: column;
    align-items: center;
    justify-content: center;
    gap: 6px;
    font-family: "Saira Semi Condensed", sans-serif;
    font-weight: 500;
    font-size: 19px;
    color: var(--ink-light);
  }
  .card-back {
    top: 631px;
    height: 470px;
    background: var(--slate);
  }
  .back-brand {
    position: absolute;
    top: 0;
    left: 0;
    right: 0;
    height: 400px;
    display: flex;
    align-items: center;
    justify-content: center;
  }
  .back-brand .brand-name {
    color: var(--ink-light);
    font-size: 44px;
  }
  .website {
    position: absolute;
    left: 0;
    right: 0;
    top: 412px;
    text-align: center;
    font-family: "Roboto", sans-serif;
    font-size: 20px;
    letter-spacing: 1.5px;
    color: var(--ink-light);
  }
</style>
</head>
<body>
<main class="canvas">
  <section class="card card-front">
    <div class="brand">
      <span class="brand-square"></span>
      <span class="brand-name">CEDAR RIDGE PROPERTY GROUP</span>
    </div>
    <div class="name-band">
      <h1 class="holder-name">Travis Lundqor CMCA</h1>
    </div>
    <div class="contact-band">
      <p class="address">812 NE Tamber Ln., Suite 9, Bend, Oregon 97815</p>
      <p class="phones">P. 541-237-4190 F. 541-237-8856</p>
    </div>
  </section>

  <section class="card card-back">
    <div class="back-brand">
      <span class="brand-name">CRPG</span>
    </div>
    <p class="website">www.cedarridgepropertygroup.com</p>
  </section>
</main>
</body>
</html>
```